Brivora Collective Business Card Design

We need a business card design for Brivora Collective. We are a healthcare recruiting, wellness and education company. We partner with medical facilities to find quality candidates. We also offer free wellness courses.
The final design should communicate an emphasis on recruiting and wellness
The main purpose of the business card is to utilized it for networking events, give to hospitals, executives, VCs surgery centers and clinics. I want it to be sleek, clean, use of our brand colors and professional.

```html
<!DOCTYPE html>
<html lang="en">
<head>
<meta charset="utf-8">
<title>Brivora Collective Business Card</title>
<link rel="stylesheet" href="https://fonts.googleapis.com/css2?family=Open+Sans:wght@400;600;700&display=swap">
<style>
  :root {
    --bg: #232323;
    --teal: #00574f;
    --teal-back: #0f6158;
    --teal-back-light: #17786c;
    --teal-deep: #0a4a43;
    --white: #ffffff;
    --radius: 22px;
  }
  * { margin: 0; padding: 0; box-sizing: border-box; }
  html, body { width: 1200px; height: 780px; overflow: hidden; }
  body {
    background: var(--bg);
    font-family: "Open Sans", Arial, sans-serif;
    display: flex;
    align-items: center;
    justify-content: center;
    gap: 40px;
  }
  .card {
    position: relative;
    width: 540px;
    height: 310px;
    border-radius: var(--radius);
    overflow: hidden;
  }
  .card-front { background: var(--teal); }
  .front-shape { position: absolute; inset: 0; width: 100%; height: 100%; }
  .contact-block {
    position: absolute;
    left: 30px;
    top: 50px;
    color: var(--white);
    white-space: nowrap;
  }
  .person-name { font-size: 23px; font-weight: 700; line-height: 1.1; }
  .person-title { font-size: 12px; font-weight: 400; margin-top: 2px; }
  .contact-list { list-style: none; margin-top: 24px; }
  .contact-item {
    display: flex;
    align-items: center;
    gap: 8px;
    font-size: 12px;
    line-height: 1.75;
  }
  .contact-icon { width: 11px; height: 11px; flex: none; }
  .front-brand {
    position: absolute;
    right: 34px;
    top: 112px;
    color: var(--teal);
    font-size: 30px;
    font-weight: 600;
    line-height: 1.05;
    text-align: right;
  }
  .card-back {
    background: linear-gradient(135deg, var(--teal-back-light) 0%, var(--teal-back) 45%, var(--teal-deep) 100%);
    display: flex;
    align-items: center;
    justify-content: center;
  }
  .back-brand {
    color: var(--teal-deep);
    font-size: 40px;
    font-weight: 600;
    line-height: 1.05;
    text-align: center;
  }
</style>
</head>
<body>
  <section class="card card-front">
    <svg class="front-shape" viewBox="0 0 540 310" preserveAspectRatio="none" aria-hidden="true">
      <path fill="#ffffff" d="M230,0 C300,0 300,150 350,220 C390,275 440,300 500,310 L540,310 L540,0 Z"/>
      <path fill="#ffffff" d="M238,12 C285,40 280,160 322,232 C348,274 380,296 410,308 C378,292 350,268 330,236 C288,166 290,48 238,12 Z"/>
    </svg>

    <div class="contact-block">
      <h1 class="person-name">Marisa Okonde</h1>
      <p class="person-title">Founder</p>
      <ul class="contact-list">
        <li class="contact-item">
          <svg class="contact-icon" viewBox="0 0 24 24" aria-hidden="true"><path fill="#fff" d="M6.6 10.8a15.1 15.1 0 0 0 6.6 6.6l2.2-2.2a1 1 0 0 1 1-.25 11.4 11.4 0 0 0 3.6.57 1 1 0 0 1 1 1V20a1 1 0 0 1-1 1A17 17 0 0 1 3 4a1 1 0 0 1 1-1h3.5a1 1 0 0 1 1 1c0 1.25.2 2.45.57 3.57a1 1 0 0 1-.25 1z"/></svg>
          (555) 014-2280
        </li>
        <li class="contact-item">
          <svg class="contact-icon" viewBox="0 0 24 24" aria-hidden="true"><g fill="none" stroke="#fff" stroke-width="2"><circle cx="12" cy="12" r="9.5"/><ellipse cx="12" cy="12" rx="4" ry="9.5"/><path d="M2.5 12h19"/></g></svg>
          www.brivoracollective.com
        </li>
        <li class="contact-item">
          <svg class="contact-icon" viewBox="0 0 24 24" aria-hidden="true"><g fill="none" stroke="#fff" stroke-width="2"><rect x="2.5" y="5" width="19" height="14" rx="1.5"/><path d="M3 6l9 7 9-7"/></g></svg>
          hello@brivoracollective.com
        </li>
      </ul>
    </div>

    <p class="front-brand">Brivora<br>Collective</p>
  </section>

  <section class="card card-back" role="img" aria-label="Brand pattern background with Brivora Collective name">
    <p class="back-brand">Brivora<br>Collective</p>
  </section>
</body>
</html>
```